New Business Card Design Project

Use the flyer uploaded and website www.brightoakbuilders.com for inspiration.
List Our Services on Backside of business cards
Martin Hollis
Harborline Renovations Inc.
Licensed General Contractors
858-471-9063

Contact Information for Business Card

Use the flyer uploaded and website www.brightoakbuilders.com for inspiration. List Our Services on Backside of business cards Martin Hollis Harborline Renovations Inc. Licensed General Contractors 858-471-9063

```html
<!DOCTYPE html>
<html lang="en">
<head>
<meta charset="utf-8">
<title>Harborline Renovations – Business Cards</title>
<link href="https://fonts.googleapis.com/css2?family=Montserrat:wght@400;500;700;800&display=swap" rel="stylesheet">
<style>
  :root {
    --backdrop: #3b3b3b;
    --backdrop-dark: #262626;
    --card: #151515;
    --ink: #ffffff;
    --ink-soft: #e6e6e6;
    --rule: #ffffff;
  }
  * { margin: 0; padding: 0; box-sizing: border-box; }
  html, body { width: 1200px; height: 998px; overflow: hidden; }
  body {
    background: radial-gradient(ellipse at 40% 45%, var(--backdrop) 0%, var(--backdrop-dark) 100%);
    font-family: "Montserrat", sans-serif;
    color: var(--ink);
    position: relative;
  }
  .card {
    position: absolute;
    width: 560px;
    height: 320px;
    background: var(--card);
    box-shadow: 0 14px 30px rgba(0,0,0,.55);
  }
  .card--back { left: 60px; top: 100px; }
  .card--front { left: 580px; top: 560px; }

  .brand-name {
    font-weight: 500;
    letter-spacing: 3px;
    text-transform: uppercase;
    color: var(--ink);
  }

  /* Back side */
  .card--back .brand-name {
    position: absolute; top: 58px; left: 0; right: 0;
    text-align: center; font-size: 22px;
  }
  .services-heading {
    position: absolute; top: 128px; left: 40px; right: 40px;
    display: flex; align-items: center; gap: 14px;
  }
  .services-heading .rule { flex: 1; height: 1.5px; background: var(--rule); }
  .services-heading h2 { font-size: 15px; font-weight: 800; letter-spacing: 1px; white-space: nowrap; }
  .services-list {
    position: absolute; top: 168px; left: 44px; right: 30px;
    display: grid; grid-template-columns: 1.1fr 1fr; column-gap: 18px;
  }
  .services-list ul { list-style: none; }
  .services-list li {
    display: flex; align-items: center; gap: 8px;
    font-size: 13px; line-height: 24px; color: var(--ink-soft);
  }
  .tick { width: 13px; height: 13px; flex: none; }

  /* Front side */
  .card--front .brand-name {
    position: absolute; top: 66px; left: 44px; font-size: 22px;
  }
  .person { position: absolute; left: 44px; top: 140px; }
  .person-name { font-size: 30px; font-weight: 800; }
  .person-title { font-size: 14px; font-weight: 700; margin-top: 4px; padding-bottom: 10px; border-bottom: 1.5px solid var(--rule); width: 260px; }
  .contact { list-style: none; margin-top: 14px; }
  .contact li { display: flex; align-items: center; gap: 12px; font-size: 15px; line-height: 28px; }
  .contact svg { width: 16px; height: 16px; flex: none; }
</style>
</head>
<body>

<section class="card card--back" aria-label="Business card back">
  <div class="brand-name">Harborline Renovations</div>
  <div class="services-heading">
    <span class="rule"></span><h2>OUR SERVICES</h2><span class="rule"></span>
  </div>
  <div class="services-list">
    <ul>
      <li><svg class="tick" viewBox="0 0 14 14"><rect x="1" y="1" width="12" height="12" fill="none" stroke="#fff" stroke-width="1.5"/><path d="M3.5 7l2.5 2.5L11 3.5" fill="none" stroke="#fff" stroke-width="1.8"/></svg>Remodel: Kitchen &amp; Bath</li>
      <li><svg class="tick" viewBox="0 0 14 14"><rect x="1" y="1" width="12" height="12" fill="none" stroke="#fff" stroke-width="1.5"/><path d="M3.5 7l2.5 2.5L11 3.5" fill="none" stroke="#fff" stroke-width="1.8"/></svg>Painting: Interior &amp; Exterior</li>
      <li><svg class="tick" viewBox="0 0 14 14"><rect x="1" y="1" width="12" height="12" fill="none" stroke="#fff" stroke-width="1.5"/><path d="M3.5 7l2.5 2.5L11 3.5" fill="none" stroke="#fff" stroke-width="1.8"/></svg>Flooring: Carpet, Vinyl, Wood</li>
      <li><svg class="tick" viewBox="0 0 14 14"><rect x="1" y="1" width="12" height="12" fill="none" stroke="#fff" stroke-width="1.5"/><path d="M3.5 7l2.5 2.5L11 3.5" fill="none" stroke="#fff" stroke-width="1.8"/></svg>Window &amp; Door Replacement</li>
    </ul>
    <ul>
      <li><svg class="tick" viewBox="0 0 14 14"><rect x="1" y="1" width="12" height="12" fill="none" stroke="#fff" stroke-width="1.5"/><path d="M3.5 7l2.5 2.5L11 3.5" fill="none" stroke="#fff" stroke-width="1.8"/></svg>Plumbing: Repairs &amp; Upgrades</li>
      <li><svg class="tick" viewBox="0 0 14 14"><rect x="1" y="1" width="12" height="12" fill="none" stroke="#fff" stroke-width="1.5"/><path d="M3.5 7l2.5 2.5L11 3.5" fill="none" stroke="#fff" stroke-width="1.8"/></svg>Energy-Efficient Upgrades</li>
      <li><svg class="tick" viewBox="0 0 14 14"><rect x="1" y="1" width="12" height="12" fill="none" stroke="#fff" stroke-width="1.5"/><path d="M3.5 7l2.5 2.5L11 3.5" fill="none" stroke="#fff" stroke-width="1.8"/></svg>Deck &amp; Patio Construction</li>
    </ul>
  </div>
</section>

<section class="card card--front" aria-label="Business card front">
  <div class="brand-name">Harborline Renovations</div>
  <div class="person">
    <div class="person-name">Martin Hollis</div>
    <div class="person-title">Licensed General Contractors</div>
    <ul class="contact">
      <li><svg viewBox="0 0 16 16"><path d="M4 1.5l2.5 3-1.5 1.8c.8 1.8 2.3 3.3 4.1 4.1l1.8-1.5 3 2.5-1.6 2.3C7.6 13.7 2.3 8.4 1.7 3.1z" fill="#fff"/></svg>858-471-9063</li>
      <li><svg viewBox="0 0 16 16" fill="none" stroke="#fff" stroke-width="1.4"><circle cx="8" cy="8" r="6.5"/><ellipse cx="8" cy="8" rx="3" ry="6.5"/><path d="M1.5 8h13M2.5 4.8h11M2.5 11.2h11"/></svg>www.brightoakbuilders.com</li>
    </ul>
  </div>
</section>

</body>
</html>
```